Email Marketing Design for THCA/ HEMP/ CANNABIS

Create an eye popping email friendly design for legal hemp products. Open to GIF format pictures or anything creative. I uploaded a sample design of what we are looking for with up to 10 designs along with sample GIF photos: Sky Ridge Remedy Mail - Fwd_ NEW ARRIVALS LOST...

-Create a fruit design background for the candy jars. Photoshop the label design onto the mason jar with gold lid if needed. Available flavors: watermelon, strawberry, raspberry, pineapple, orange, lemon, green apple, grape, cherry, blue raspberry.

-Create a gif or email friendly design for the 1gram my display images using the product pictures.

-Mossfern 3.5 grams premium flower: use design of the label picture of the jar with picture of the bud (use the picture of the Jar uploaded in the brief)

-Mossfern 3.5 snowrock use design of the label picture of the jar with picture of the white bud (use the picture of the Jar uploaded in the brief)

Additional SKU's

-Pre roll box and tubes:
place display graphics onto the acrylic box (Mossfern Pre-Roll 16 Count Display)
place the pre roll graphics onto the pre roll tube (Mossfern 1.5 Gram 16 Count Pre-roll Inner)
Create a GIF for this product with the submitted graphics

-Pocket Tub Zippers
Place the design (Mossferns_Tin_13Flavours_UpdatedFlavors_PrintReady) (front side of the graphics) onto the tin can photo

-Little Orbit Jars
Place the little orbit design (LITTLE ORBITS - THCA) onto the jar picture

-Mossfern 2 pack regular pre roll (non white coated)
Create a GIF for this prodcut with the submitted graphics
(please use the front side of the packaging design only)

-Mossfern 2 pack snow pre roll (white coated)
created a GIF for this product with the submitted graphics

Target Market(s)

21-45 years old

Industry/Entity Type

hemp

Requirements
Must have
• Eye popping designs
Nice to have
• gif style format
Should not have
• generic product pictures

```html
<!DOCTYPE html>
<html lang="en">
<head>
<meta charset="utf-8">
<title>Mossfern Hemp Candies</title>
<link rel="stylesheet" href="https://fonts.googleapis.com/css2?family=Open+Sans:wght@300;400;600;700&family=Montserrat:wght@600;700&family=Arimo:wght@400;700&family=Merriweather:wght@700&display=swap">
<style>
:root{
  --black:#050505;
  --cream:#f6eddf;
  --coral:#f24d3f;
  --coral-text:#ee4f3d;
  --ink:#333333;
  --white:#ffffff;
  --forest:#2f5a2a;
  --forest-dark:#0f2c12;
  --table-head:#e9e9e9;
  --sketch:rgba(232,110,84,.16);
}
*{box-sizing:border-box;margin:0;padding:0}
html,body{width:1200px;height:4755px;overflow:hidden}
body{font-family:'Open Sans',sans-serif;background:var(--cream);color:var(--ink)}
.canvas{position:relative;width:1200px;height:4755px}
section{position:absolute;left:0;width:1200px;overflow:hidden}
.btn{position:absolute;display:flex;align-items:center;justify-content:center;width:268px;height:53px;border-radius:27px;font-family:'Montserrat',sans-serif;font-weight:700;font-size:20px;letter-spacing:1px;text-decoration:none}
.btn-coral{background:var(--coral);color:var(--white)}
.btn-white{background:var(--white);color:var(--coral)}
.fruit-sketch{position:absolute;border-radius:40%;background:var(--sketch)}

/* hero */
.hero{top:0;height:665px;background:var(--black)}
.hero-visual{position:absolute;left:563px;top:22px;width:637px;height:643px;
  background:
   radial-gradient(ellipse 150px 230px at 52% 47%,rgba(120,200,60,.95),rgba(70,140,40,.6) 55%,rgba(0,0,0,0) 100%),
   radial-gradient(circle at 80% 30%,rgba(110,60,150,.85),rgba(0,0,0,0) 35%),
   radial-gradient(circle at 22% 68%,rgba(95,50,120,.8),rgba(0,0,0,0) 30%),
   radial-gradient(circle at 30% 25%,rgba(150,200,80,.6),rgba(0,0,0,0) 22%),
   linear-gradient(160deg,#1c1f22,#0c0d0f)}
.brand{position:absolute;left:74px;top:55px;display:flex;align-items:center}
.brand-dot{width:107px;height:107px;border-radius:50%;background:#1c3a2a;display:flex;align-items:center;justify-content:center;color:var(--white);font-size:16px;font-weight:600}
.hero h1{position:absolute;left:66px;top:188px;font-weight:400;font-size:70px;line-height:80px;color:var(--white);z-index:2;white-space:nowrap}
.hero p{position:absolute;left:68px;top:380px;width:600px;font-size:24px;line-height:32px;color:var(--white)}
.hero .btn{left:70px;top:522px}

/* intro */
.intro{top:665px;height:660px;background:var(--cream);text-align:center}
.intro h2{position:absolute;left:0;width:1200px;top:52px;font-weight:400;font-size:50px;color:var(--ink)}
.intro p{position:absolute;left:100px;width:1000px;top:128px;font-size:19px;line-height:25.5px;color:var(--ink)}
.flavor{position:absolute;top:326px;width:300px;text-align:center;font-family:'Arimo',sans-serif;color:#444}
.flavor-photo{width:200px;height:200px;border-radius:50%;margin:0 auto 10px}
.flavor b{display:block;font-weight:400;font-size:36px;line-height:42px}
.flavor span{display:block;font-size:32px;line-height:42px}

/* hemp extract */
.extract{top:1325px;height:663px;background:var(--coral)}
.fruit-circle{position:absolute;left:132px;top:143px;width:394px;height:394px;border-radius:50%;
  background:
   radial-gradient(circle at 72% 62%,#ffb72c 0%,#f8921e 16%,rgba(248,146,30,0) 30%),
   radial-gradient(circle at 70% 25%,#ef4b55 0%,rgba(239,75,85,0) 28%),
   radial-gradient(circle at 28% 40%,#f3b531 0%,rgba(243,181,49,0) 30%),
   radial-gradient(circle at 35% 78%,#2c56c9 0%,rgba(44,86,201,0) 30%),
   radial-gradient(circle at 55% 88%,#d62d5c 0%,rgba(214,45,92,0) 25%),
   linear-gradient(135deg,#3f8d2e,#2a6b25 60%,#6b2b5c)}
.extract h2{position:absolute;left:637px;top:118px;font-weight:400;font-size:60px;line-height:74px;color:var(--white)}
.extract p{position:absolute;left:640px;top:297px;width:480px;font-family:'Arimo',sans-serif;font-size:24px;line-height:30px;color:var(--white)}
.extract .btn{left:640px;top:442px}

/* orange */
.orange{top:1988px;height:667px;background:var(--cream)}
.orange h2{position:absolute;left:60px;width:510px;top:134px;text-align:center;font-weight:400;font-size:60px;line-height:74px;color:var(--coral-text)}
.orange p{position:absolute;left:40px;width:550px;top:300px;text-align:center;font-size:23px;line-height:30px;color:var(--coral-text)}
.orange .btn{left:181px;top:447px}
.orange-visual{position:absolute;left:689px;top:150px;width:394px;height:394px;border-radius:50%;
  background:
   radial-gradient(ellipse 110px 150px at 50% 52%,#3a2a24 0%,#7a3d1e 60%,rgba(122,61,30,0) 100%),
   radial-gradient(circle at 85% 55%,#ff9a1c,rgba(255,154,28,0) 30%),
   radial-gradient(circle at 15% 60%,#ffb23a,rgba(255,178,58,0) 30%),
   linear-gradient(160deg,#f29a2e,#e36a1d)}

/* strawberry */
.strawberry{top:2655px;height:664px;background:var(--coral)}
.strawberry-visual{position:absolute;left:0;top:0;width:665px;height:664px;
  background:
   radial-gradient(ellipse 150px 230px at 50% 52%,#4a1c1e 0%,#8a2126 60%,rgba(138,33,38,0) 100%),
   radial-gradient(circle at 20% 70%,#d0262c,rgba(208,38,44,0) 22%),
   radial-gradient(circle at 80% 68%,#d0262c,rgba(208,38,44,0) 22%),
   radial-gradient(circle at 50% 28%,#c3202a,rgba(195,32,42,0) 35%),
   linear-gradient(160deg,#e8b0ae,#d9817f 55%,#e9bcba)}
.strawberry h2{position:absolute;left:680px;width:505px;top:208px;text-align:center;font-weight:400;font-size:50px;line-height:62px;color:var(--white)}
.strawberry p{position:absolute;left:700px;width:480px;top:347px;text-align:center;font-size:19px;line-height:25px;color:var(--white)}

/* ingredients */
.facts{top:3319px;height:691px;background:var(--cream);color:var(--coral-text)}
.facts h2{position:absolute;left:0;width:1200px;top:56px;text-align:center;font-weight:400;font-size:66px}
.facts-body{position:absolute;left:68px;top:165px;width:900px;font-size:19px;line-height:25px}
.facts-body strong{font-weight:700}
.facts-body .block{margin-bottom:17px}
.nutrition{border-collapse:collapse;width:889px;margin:12px 0 14px;font-family:'Arimo',sans-serif;color:#111;font-size:18px}
.nutrition th,.nutrition td{text-align:left;padding:8px 4px;border:1px solid #dcdcdc;height:40px}
.nutrition th{background:var(--table-head);font-weight:700}
.nutrition td{background:var(--white)}

/* testimonial */
.testimonial{top:4010px;height:670px;background:linear-gradient(180deg,#2f5a2a,#3e6a32 50%,#2c5226)}
.testimonial-bg{position:absolute;left:0;top:0;width:1200px;height:670px;
  background:
   radial-gradient(ellipse 260px 330px at 50% 55%,rgba(90,130,70,.7),rgba(30,70,30,0) 100%),
   radial-gradient(circle at 10% 20%,rgba(80,130,60,.55),rgba(0,0,0,0) 22%),
   radial-gradient(circle at 90% 85%,rgba(80,130,60,.55),rgba(0,0,0,0) 22%)}
.tag{position:absolute;left:910px;top:30px;font-family:'Merriweather',serif;font-weight:700;font-size:25px;color:#8fae7c}
.testimonial blockquote{position:absolute;left:260px;width:680px;top:245px;text-align:center;font-family:'Arimo',sans-serif;font-weight:700;font-size:30px;line-height:37px;color:var(--white)}
.testimonial cite{position:absolute;left:0;width:1200px;top:410px;text-align:center;font-family:'Merriweather',serif;font-weight:700;font-style:normal;font-size:34px;color:var(--white)}

/* footer */
.footer{top:4680px;height:75px;background:var(--forest-dark);display:flex;align-items:center;justify-content:center;color:var(--white);font-family:'Arimo',sans-serif;font-size:20px;letter-spacing:1.5px}
</style>
</head>
<body>
<div class="canvas">

  <section class="hero">
    <div class="hero-visual" role="img" aria-label="Grape hemp candy jar surrounded by grapes, sugared gummies and hemp leaves on a dark background"></div>
    <div class="brand"><div class="brand-dot">Mossfern</div></div>
    <h1>Indulge in the<br>Sweetness of Nature</h1>
    <p>Experience the Perfect Blend of Sweetness and<br>Wellness with Mossfern's Grape-Flavored Hemp<br>Candies!</p>
    <a class="btn btn-coral" href="#">ORDER NOW</a>
  </section>

  <section class="intro">
    <div class="fruit-sketch" style="left:28px;top:40px;width:150px;height:85px" role="img" aria-label="Line sketch of apples"></div>
    <div class="fruit-sketch" style="left:830px;top:25px;width:92px;height:75px" role="img" aria-label="Line sketch of a lemon"></div>
    <div class="fruit-sketch" style="left:1045px;top:200px;width:135px;height:135px" role="img" aria-label="Line sketch of cherries"></div>
    <div class="fruit-sketch" style="left:738px;top:250px;width:82px;height:82px" role="img" aria-label="Line sketch of an orange"></div>
    <div class="fruit-sketch" style="left:30px;top:430px;width:118px;height:168px" role="img" aria-label="Line sketch of a pineapple"></div>
    <h2>Dear Customer,</h2>
    <p>We are thrilled to introduce Mossfern's latest treat: sugar-coated, grape-flavored hemp candies.<br>Our candies combine the refreshing taste of natural benefits of hemp, creating an irresistible delight for<br>your taste buds. Additionally, we offer a variety of flavors including watermelon, strawberry, raspberry,<br>pineapple, orange, lemon, green apple, grape, cherry, and blue raspberry, ensuring there's a perfect flavor<br>for everyone to enjoy.</p>
    <div class="flavor" style="left:112px"><div class="flavor-photo" role="img" aria-label="Orange flavor candy jar" style="background:radial-gradient(ellipse 45px 70px at 50% 55%,#f07a22,#b4521c 60%,rgba(0,0,0,0) 100%),linear-gradient(160deg,#5a5d60,#1c1d1f)"></div><b>ORANGE</b><span>Flavor</span></div>
    <div class="flavor" style="left:437px"><div class="flavor-photo" role="img" aria-label="Natural flavor candy jar with gold lid" style="background:radial-gradient(ellipse 50px 65px at 50% 55%,#b08a4a,#5b4426 60%,rgba(0,0,0,0) 100%),linear-gradient(160deg,#3a3026,#151210)"></div><b>NATURAL</b><span>Flavor</span></div>
    <div class="flavor" style="left:788px"><div class="flavor-photo" role="img" aria-label="Watermelon flavor candy jar" style="background:radial-gradient(ellipse 50px 70px at 50% 55%,#e85a66,#b72a36 60%,rgba(0,0,0,0) 100%),linear-gradient(160deg,#33474a,#182224)"></div><b>WATERMELON</b><span>Flavor</span></div>
  </section>

  <section class="extract">
    <div class="fruit-circle" role="img" aria-label="Colourful fruit arrangement with pineapple, watermelon, orange and berries"></div>
    <h2>Rich in natural<br>hemp extract</h2>
    <p>Lorem ipsum dolor sit amet, consectetur adipiscing elit. Vivamus lacinia odio vitae vestibulum vestibulum.</p>
    <a class="btn btn-white" href="#">ORDER NOW</a>
  </section>

  <section class="orange">
    <div class="fruit-sketch" style="left:500px;top:50px;width:152px;height:88px" role="img" aria-label="Line sketch of apples"></div>
    <div class="fruit-sketch" style="left:1040px;top:60px;width:92px;height:72px" role="img" aria-label="Line sketch of a lemon"></div>
    <div class="fruit-sketch" style="left:48px;top:480px;width:118px;height:162px" role="img" aria-label="Line sketch of a pineapple"></div>
    <div class="fruit-sketch" style="left:520px;top:515px;width:84px;height:84px" role="img" aria-label="Line sketch of an orange"></div>
    <div class="fruit-sketch" style="left:1048px;top:500px;width:132px;height:132px" role="img" aria-label="Line sketch of cherries"></div>
    <h2>100% Orange<br>Flavor</h2>
    <p>Ingredients: Pure Cane Sugar, Natural Orange-<br>Flavor, Hemp Extract, Natural Colors, Citric<br>Acid, Organic Tapioca Syrup.</p>
    <a class="btn btn-coral" href="#">ORDER NOW</a>
    <div class="orange-visual" role="img" aria-label="Orange flavor candy jar with orange slices and splashes"></div>
  </section>

  <section class="strawberry">
    <div class="strawberry-visual" role="img" aria-label="Strawberry flavor candy jar with strawberries, leaves and red juice splash"></div>
    <h2>100% Strawberry<br>Flavor</h2>
    <p>We are thrilled to introduce Mossfern's latest<br>treat and best in the market</p>
  </section>

  <section class="facts">
    <h2>Ingredients:</h2>
    <div class="facts-body">
      <div class="block"><strong>Ingredients:</strong> Pure Cane Sugar, Natural Grape Flavor, Hemp Extract, Natural Colors, Citric<br>Acid, Organic Tapioca Syrup.</div>
      <div><strong>Nutritional Information:</strong></div>
      <table class="nutrition">
        <colgroup><col style="width:138px"><col style="width:114px"><col style="width:113px"><col style="width:111px"><col style="width:225px"><col style="width:102px"><col style="width:86px"></colgroup>
        <tr><th>Serving Size</th><th>Calories</th><th>Total Fat</th><th>Sodium</th><th>Total Carbohydrates</th><th>Sugars</th><th>Protein</th></tr>
        <tr><td>10 candies</td><td>50</td><td>0g</td><td>5mg</td><td>13g</td><td>12g</td><td>0g</td></tr>
      </table>
      <div class="block"><strong>Health Claims:</strong><br>Rich in natural hemp extract</div>
      <div class="block"><strong>Usage Instructions:</strong><br>Enjoy as a sweet treat. Do not exceed the recommended serving size.</div>
      <div class="block"><strong>Storage Instructions:</strong><br>Store in a cool, dry place. Keep the jar tightly closed to maintain freshness.</div>
      <div class="block"><strong>Allergen Information:</strong><br>Allergen Information: Produced in a facility that processes nuts and dairy.</div>
    </div>
  </section>

  <section class="testimonial">
    <div class="testimonial-bg" role="img" aria-label="Faded green candy jar with hemp leaves in the background"></div>
    <div class="tag">Hemp Cands</div>
    <blockquote>Lorem ipsum dolor sit amet, consectetur adipiscing elit. Vivamus lacinia odio vitae vestibulum vestibulum.</blockquote>
    <cite>Corin Adler</cite>
  </section>

  <section class="footer">Produced by: Mossfern Co., 48 Meadow Row, Brookvale, USA</section>

</div>
</body>
</html>
```